Hot-air ballooning company needs a DL-size flyer

Skylark Aerial Tours is a hot-air ballooning company which flies passengers in the King Valley, Victoria, Australia.
We need a 2-sided DL-size flyer which promotes our hot-air balloon flights and packages.
Most of our customers are couples, and we want the flyer design to communicate safety, adventure, and romance.
The flyer should make the best use of our images which we provide, and we've also included a document with the text for the flyer.
Updates

2 days is not long enough to gather designs, the brief never asked me what my deadline should be.

Target Market(s)

Couples, buyers are majority female, between the ages of 20-60

Industry/Entity Type

Tourism

Font styles to use
Sans Serif

Colors

Designer to choose colors to be used in the design.

Requirements
Must have
• Communicate safety, adventure, and romance
• Use images
Nice to have
• There is a lot of text, it would be great if you could make it look like as little text as possible
Should not have
• No childish designs

```html
<!DOCTYPE html>
<html lang="en">
<head>
<meta charset="utf-8">
<title>Skylark Aerial Tours — Flyer</title>
<link rel="stylesheet" href="https://fonts.googleapis.com/css2?family=Arimo:ital,wght@0,700;1,400&display=swap">
<style>
  :root {
    --panel-blue: #5f8dbf;
    --frame-white: #ffffff;
    --title-red: #e2305a;
    --text-white: #ffffff;
    --sky-top: #4f8fd0;
    --haze: #dfe4e6;
    --vine-dark: #3a2e28;
    --field-green: #5f7a45;
    --dusk-blue: #3f5876;
    --warm-orange: #d9783a;
  }
  * { box-sizing: border-box; margin: 0; padding: 0; }
  html, body { width: 1200px; height: 2525px; overflow: hidden; background: var(--panel-blue); }
  .flyer {
    position: relative;
    width: 1200px;
    height: 2525px;
    background: var(--panel-blue);
    font-family: "Arimo", Arial, sans-serif;
    color: var(--text-white);
  }
  .headline {
    position: absolute;
    top: 48px; left: 0; width: 1200px;
    text-align: center;
    font-family: "Arimo", Arial, sans-serif;
    font-weight: 700;
    font-size: 106px;
    line-height: 96px;
    color: var(--title-red);
    -webkit-text-stroke: 9px var(--frame-white);
    paint-order: stroke fill;
  }
  .tagline {
    position: absolute;
    top: 270px; left: 0; width: 1200px;
    text-align: center;
    font-style: italic;
    font-weight: 400;
    font-size: 82px;
    line-height: 92px;
    color: var(--text-white);
  }
  .photo {
    position: absolute;
    border: 6px solid var(--frame-white);
  }
  .photo--balloon-dawn {
    left: -6px; top: 500px; width: 672px; height: 816px;
    background: linear-gradient(180deg, #6f9fcf 0%, #a9c6df 55%, #d8dfe3 82%, #6d6a5a 100%);
  }
  .photo--vineyard-flight {
    left: 544px; top: 1316px; width: 662px; height: 1215px;
    background: linear-gradient(180deg, var(--sky-top) 0%, #8fb7dc 45%, var(--haze) 62%, #9a9a88 72%, var(--field-green) 80%, var(--vine-dark) 100%);
  }
  .photo--burner-glow {
    left: -6px; top: 2008px; width: 556px; height: 523px;
    background: linear-gradient(180deg, var(--warm-orange) 0%, #b8603a 40%, var(--dusk-blue) 75%, #2c3240 100%);
  }
  .text-panel {
    position: absolute;
    border: 6px solid var(--frame-white);
    background: var(--panel-blue);
  }
  .text-panel--intro { left: 660px; top: 500px; width: 546px; height: 816px; }
  .text-panel--details { left: -6px; top: 1310px; width: 556px; height: 704px; }
  .feature {
    position: absolute;
    font-weight: 700;
    font-size: 38px;
    line-height: 46px;
    color: var(--text-white);
    white-space: nowrap;
  }
  .feature .pin {
    position: absolute;
    left: -40px; top: 2px;
    width: 36px; height: 46px;
  }
  .feature .note { font-weight: 400; font-style: italic; }
</style>
</head>
<body>
<main class="flyer">
  <h1 class="headline">SKYLARK AERIAL<br>TOURS</h1>
  <p class="tagline">The perfect gourmet<br>ballooning experience</p>

  <div class="photo photo--balloon-dawn" role="img" aria-label="Colourful striped hot-air balloon rising at dawn over misty countryside"></div>

  <section class="text-panel text-panel--intro">
    <p class="feature" style="left:52px; top:12px;">
      <svg class="pin" viewBox="0 0 36 46"><path d="M18 0C8 0 0 8 0 18c0 13 18 28 18 28s18-15 18-28C36 8 28 0 18 0z" fill="#fff"/></svg>
      Live the romance and<br>adventure of flying the<br>beautiful King Valley<br>and surrounds in a hot-<br>air balloon at dawn
    </p>
    <p class="feature" style="left:52px; top:263px;">
      <svg class="pin" viewBox="0 0 36 46"><path d="M18 0C8 0 0 8 0 18c0 13 18 28 18 28s18-15 18-28C36 8 28 0 18 0z" fill="#fff"/></svg>
      From the vineyards<br>and patchwork of fields<br>the views expand<br>to the Ovens River,<br>spectacular Mt Buffalo<br>and the High Country<br>beyond
    </p>
    <p class="feature" style="left:52px; top:605px;">
      <svg class="pin" viewBox="0 0 36 46"><path d="M18 0C8 0 0 8 0 18c0 13 18 28 18 28s18-15 18-28C36 8 28 0 18 0z" fill="#fff"/></svg>
      The mountain views,<br>once aloft, come to life<br>in dramatic 3D with the<br>early morning light
    </p>
  </section>

  <section class="text-panel text-panel--details">
    <p class="feature" style="left:76px; top:30px;">
      <svg class="pin" viewBox="0 0 36 46"><path d="M18 0C8 0 0 8 0 18c0 13 18 28 18 28s18-15 18-28C36 8 28 0 18 0z" fill="#fff"/></svg>
      Celebrate your flight<br>with a delicious<br>breakfast afterwards<br><span class="note">(optional)</span>
    </p>
    <p class="feature" style="left:76px; top:274px;">
      <svg class="pin" viewBox="0 0 36 46"><path d="M18 0C8 0 0 8 0 18c0 13 18 28 18 28s18-15 18-28C36 8 28 0 18 0z" fill="#fff"/></svg>
      Milawa is conveniently<br>located less than an<br>hour’s drive from most<br>places in Victoria’s<br>North East and Albury<br>in NSW
    </p>
    <p class="feature" style="left:76px; top:572px;">
      <svg class="pin" viewBox="0 0 36 46"><path d="M18 0C8 0 0 8 0 18c0 13 18 28 18 28s18-15 18-28C36 8 28 0 18 0z" fill="#fff"/></svg>
      Mansfield flights are<br>also available
    </p>
  </section>

  <div class="photo photo--vineyard-flight" role="img" aria-label="Three hot-air balloons flying over misty vineyards and a winery at sunrise"></div>
  <div class="photo photo--burner-glow" role="img" aria-label="Inflated balloon lit at dusk with guests gathered before take-off"></div>
</main>
</body>
</html>
```